home accents e-commerce website

I'd like a professional simple website designed where I can sell my home goods. I already have my domain name registered. I need the website to accept credit card payments and Tendrix. It should have a shopping cart option and calculate sales tax and shipping costs on merchandise automatically.

I'll be taking photographs of the merchandise and writing product descriptions myself. (I'm not a professional photographer, so these photos probably won't look too polished. If you can help me make them look better, that'd be great). As I add new merchandise in the future, I'd like an option where I can log in to the back end myself and add pictures/product descriptions. And take old products down as they sell out. So the website needs to be user-friendly for me, even though I'm completely web design illiterate!

I'd like a creative, talented person who can create a whimsical, cute website. Nothing too corporate-looking.

Thank you!

Target Market(s)

women, online shoppers, New York City-area, (ship products to the United States only)

Industry/Entity Type

Home And Garden

Coding

Coded - Design and coding required

Number of Pages Required

1 page

Font styles to use
Sans Serif

Colors
0355a3
ffffff

Requirements
Must have
• shopping cart feature
• safe, secure credit card and Tendrix payments
• ability for me to go in and add new products and take down old/sold products
Nice to have
• whimsical, cute design
Should not have
• too corporate-looking

```html
<!DOCTYPE html>
<html lang="en">
<head>
<meta charset="utf-8">
<title>Norla Home Goods</title>
<link rel="stylesheet" href="https://fonts.googleapis.com/css2?family=Jost:wght@400;500;600&display=swap">
<style>
:root{
  --blue:#0355a3;
  --white:#ffffff;
  --ink:#222222;
  --text:#555555;
  --muted:#8a8a8a;
  --line:#dddddd;
  --black:#111111;
  --footer:#1c1c1c;
  --band:#a3a3a3;
  --hover-grey:#9b9b9b;
}
*{box-sizing:border-box;margin:0;padding:0}
html,body{width:1200px;height:3077px;overflow:hidden;background:var(--white);font-family:"Jost",sans-serif;color:var(--ink)}
.page{position:relative;width:1200px;height:3077px}
.abs{position:absolute}
svg{display:block}

.topbar{top:0;left:0;width:1200px;height:41px;border-bottom:1px solid #eee}
.topbar .contact{position:absolute;right:250px;top:12px;display:flex;gap:26px;font-size:15px;color:var(--text)}
.topbar .contact span{display:flex;align-items:center;gap:8px}
.social{display:flex;gap:8px}
.social i{display:block;width:26px;height:26px;background:var(--ink)}
.topbar .social{position:absolute;right:98px;top:7px}

.logo{top:41px;left:98px;width:220px;height:92px;background:#f4f4f4;display:flex;flex-direction:column;justify-content:center;align-items:center}
.logo .name{font-size:54px;font-weight:500;color:var(--blue);line-height:1;letter-spacing:1px}
.logo .sub{font-size:17px;font-weight:500;color:var(--blue);letter-spacing:7px;margin-top:4px}
.tools{top:73px;right:98px;display:flex;gap:8px;align-items:center}
.tool{height:31px;min-width:38px;background:var(--ink);color:var(--white);display:flex;align-items:center;justify-content:center;gap:4px;font-size:12px;padding:0 6px}
.tool b{background:var(--blue);padding:1px 4px;font-weight:500}
.cart{display:flex;align-items:center;gap:10px;font-size:13px;color:var(--text)}
.cart .tool{background:var(--blue)}

.nav{top:137px;left:0;width:1200px;height:52px;background:var(--black)}
.nav ul{position:absolute;left:98px;top:0;display:flex;list-style:none;height:52px}
.nav li{color:var(--white);font-size:15px;display:flex;align-items:center;padding:0 26px;border-right:1px solid #333}
.nav li.active{background:var(--blue);width:101px;justify-content:center}
.search{position:absolute;left:781px;top:0;width:320px;height:52px;display:flex}
.search .field{flex:1;background:#2a2a2a;color:#9a9a9a;font-size:13px;display:flex;align-items:center;padding-left:16px}
.search .btn{width:52px;background:var(--blue);display:flex;align-items:center;justify-content:center}

.cats{top:222px;left:98px;width:259px;height:430px;border:1px solid var(--line)}
.cats h3{height:51px;background:#2b2b2b;color:var(--white);font-size:17px;font-weight:500;display:flex;align-items:center;gap:12px;padding-left:16px;margin:-1px}
.cats ul{list-style:none;padding:8px 28px 0 26px}
.cats li{font-size:15px;color:var(--text);height:38.4px;display:flex;align-items:center;gap:12px;border-bottom:1px solid #eee}
.cats li:last-child{border-bottom:none}
.cats li::before{content:"›";color:var(--muted)}

.hero{top:222px;left:388px;width:713px;height:430px;background:linear-gradient(90deg,#b7b3ae 0%,#6e6c6a 35%,#2b2b2e 62%,#17181b 100%)}
.hero .text{position:absolute;left:458px;top:76px;color:var(--white);font-size:48px;line-height:53px;font-weight:400;letter-spacing:1px}
.hero .badge{position:absolute;left:600px;top:100px;width:66px;height:66px;border-radius:50%;background:var(--blue);color:var(--white);text-align:center;font-size:22px;line-height:22px;padding-top:11px;font-weight:500}
.hero .badge small{display:block;font-size:17px}
.hero .shop{position:absolute;left:458px;top:252px;width:194px;height:46px;background:var(--blue);color:var(--white);font-size:19px;display:flex;align-items:center;justify-content:center}
.dots{position:absolute;right:30px;bottom:22px;display:flex;gap:6px}
.dots i{width:10px;height:10px;border-radius:50%;background:#777}
.dots i:first-child{background:var(--white)}

.banner{top:687px;width:318px;height:211px}
.banner .label{position:absolute;left:0;right:0;top:90px;height:48px;background:rgba(90,90,90,.55);color:var(--white);font-size:24px;display:flex;align-items:center;justify-content:center}

.wave{left:98px;width:1003px;height:10px}

.section-title{left:0;width:1200px;font-size:32px;font-weight:400;color:var(--ink);display:flex;justify-content:center;align-items:center;gap:26px}
.section-title::before,.section-title::after{content:"";width:130px;height:1px;background:var(--line)}
.section-title em{font-style:normal;color:var(--blue)}

.tabs{top:1081px;left:0;width:1200px;display:flex;justify-content:center;font-size:17px;color:var(--text)}
.tabs span{padding:0 26px;height:38px;display:flex;align-items:center;border-right:1px solid var(--line)}
.tabs span:last-child{border-right:none}
.tabs span.on{border:1px solid #bbb;width:101px;justify-content:center;margin-right:26px}

.product{width:231px;height:366px;border:1px solid var(--line);background:var(--white)}
.product .img{height:225px}
.product .rate{margin:26px auto 0;width:184px;display:flex;align-items:center;gap:8px}
.product .rate::before,.product .rate::after{content:"";flex:1;height:1px;background:var(--line)}
.stars{display:flex;gap:2px}
.stars svg{width:12px;height:12px}
.star-on{fill:var(--blue)}
.star-off{fill:none;stroke:#999;stroke-width:1.5}
.pname{text-align:center;font-size:16px;margin-top:10px;color:var(--ink)}
.price{display:flex;gap:14px;justify-content:center;font-size:18px;margin-top:14px}
.price s{color:var(--muted)}
.price b{font-weight:400;color:var(--blue)}
.product.active{border-color:var(--blue)}
.ribbon{position:absolute;right:0;top:0;width:60px;height:60px;clip-path:polygon(0 0,100% 0,100% 100%);background:var(--blue)}
.ribbon span{position:absolute;right:-2px;top:14px;transform:rotate(45deg);color:var(--white);font-size:13px;width:60px;text-align:center}
.actions{top:1914px;left:98px;width:231px;height:41px;display:flex;gap:2px}
.actions i{flex:1;background:var(--hover-grey);display:flex;align-items:center;justify-content:center}
.actions i:last-child{background:var(--blue)}

.viewall{top:1957px;left:502px;width:195px;height:47px;background:var(--ink);color:var(--white);font-size:19px;font-weight:500;display:flex;align-items:center;justify-content:center}

.deal{top:2193px;width:489px;height:221px;border:1px solid var(--line)}
.deal .img{position:absolute;left:8px;top:8px;width:238px;height:205px}
.deal .body{position:absolute;left:262px;right:14px;top:30px;text-align:center}
.deal .body .stars{justify-content:center}
.deal .body .pname{margin-top:16px}
.deal .desc{font-size:13px;color:var(--text);line-height:21px;margin-top:12px}

.band{top:2467px;left:0;width:1200px;height:160px;background:var(--band)}
.feature{top:2520px;width:231px;height:56px;background:var(--white);display:flex;align-items:center;gap:14px;padding-left:18px;font-size:13px;color:var(--ink);line-height:17px}
.feature.main{color:var(--blue);border-bottom:3px solid var(--blue)}

.footer{top:2627px;left:0;width:1200px;height:388px;background:var(--footer);color:#cfcfcf}
.flogo{position:absolute;left:98px;top:56px;color:#e6e6e6}
.flogo .name{font-size:52px;font-weight:500;line-height:1;letter-spacing:1px}
.flogo .sub{font-size:17px;font-weight:500;letter-spacing:7px;margin-top:2px}
.about{position:absolute;left:98px;top:142px;width:322px;font-size:13px;line-height:21px}
.fcol{position:absolute;top:100px;font-size:13px}
.fcol h4{font-size:14px;font-weight:500;color:var(--white);margin-bottom:18px}
.fcol li{list-style:none;height:26px;color:#bbbbbb}
.fcol li::before{content:"› "}
.fcol .addr{display:flex;gap:10px;line-height:18px;margin-bottom:14px}
.news{position:absolute;left:98px;top:318px;display:flex;align-items:center;gap:14px}
.news .mailbox{width:40px;height:40px;background:var(--blue);display:flex;align-items:center;justify-content:center}
.news .label{font-size:24px;color:var(--white);margin-right:10px}
.news .input{width:320px;height:37px;background:var(--white);color:#999;font-size:13px;display:flex;align-items:center;padding-left:12px}
.news .signup{width:121px;height:37px;background:var(--blue);color:var(--white);font-size:16px;font-weight:500;display:flex;align-items:center;justify-content:center;margin-left:-8px}
.footer .social{position:absolute;right:98px;top:320px;gap:10px}
.footer .social i{width:37px;height:37px;background:var(--white)}

.bottom{top:3015px;left:98px;width:1003px;height:62px;display:flex;align-items:center;justify-content:space-between;font-size:14px;color:var(--ink)}
.payments{display:flex;gap:18px;font-size:15px;font-weight:600;color:var(--blue)}
</style>
</head>
<body>
<svg width="0" height="0" style="position:absolute">
  <defs>
    <symbol id="star" viewBox="0 0 24 24"><path d="M12 2l3 7h7l-6 5 2 8-6-4-6 4 2-8-6-5h7z"/></symbol>
    <pattern id="wavy" width="10" height="10" patternUnits="userSpaceOnUse"><path d="M0 5 Q2.5 1 5 5 T10 5" fill="none" stroke="#bbb" stroke-width="1.3"/></pattern>
  </defs>
</svg>
<div class="page">

  <div class="abs topbar">
    <div class="contact">
      <span><svg width="14" height="14" viewBox="0 0 24 24"><path fill="#333" d="M6.6 10.8a15 15 0 0 0 6.6 6.6l2.2-2.2c.3-.3.7-.4 1-.2 1.1.4 2.3.6 3.6.6.6 0 1 .4 1 1V20c0 .6-.4 1-1 1A17 17 0 0 1 3 4c0-.6.4-1 1-1h3.5c.6 0 1 .4 1 1 0 1.3.2 2.5.6 3.6.1.3 0 .7-.2 1z"/></svg>+1 555 014 2290</span>
      <span><svg width="15" height="12" viewBox="0 0 24 18"><rect x="1" y="1" width="22" height="16" fill="#333"/><path d="M1 1l11 9 11-9" stroke="#fff" stroke-width="2" fill="none"/></svg>info@norlahome.com</span>
    </div>
    <div class="social"><i></i><i></i><i></i><i></i></div>
  </div>

  <div class="abs logo">
    <div class="name">norla</div>
    <div class="sub">HOME GOODS</div>
  </div>

  <div class="abs tools">
    <div class="tool"><svg width="14" height="14" viewBox="0 0 24 24"><path fill="#fff" d="M6 10V7a6 6 0 0 1 12 0v3h2v12H4V10zm3 0h6V7a3 3 0 0 0-6 0z"/></svg></div>
    <div class="tool"><svg width="13" height="12" viewBox="0 0 24 22"><path fill="#fff" d="M12 21 2 11a5.5 5.5 0 0 1 10-7 5.5 5.5 0 0 1 10 7z"/></svg><b>0</b></div>
    <div class="tool"><svg width="13" height="13" viewBox="0 0 24 24"><path fill="none" stroke="#fff" stroke-width="2.5" d="M4 8h13l-3-3M20 16H7l3 3"/></svg><b>0</b></div>
    <div class="cart">
      <div class="tool"><svg width="16" height="14" viewBox="0 0 24 22"><path fill="#fff" d="M1 1h4l3 12h12l3-9H7"/><circle cx="9" cy="19" r="2" fill="#fff"/><circle cx="19" cy="19" r="2" fill="#fff"/></svg></div>
      <span>(0)items - $0.00</span>
    </div>
  </div>

  <nav class="abs nav">
    <ul>
      <li class="active">HOME</li>
      <li>ABOUT NORLA</li>
      <li>HOW DOES THIS CRAZINESS WORK?</li>
      <li>CONTACT US</li>
    </ul>
    <div class="search">
      <div class="field">Type Keyword...</div>
      <div class="btn"><svg width="18" height="18" viewBox="0 0 24 24"><circle cx="10" cy="10" r="7" fill="none" stroke="#fff" stroke-width="3"/><path d="M15 15l7 7" stroke="#fff" stroke-width="3"/></svg></div>
    </div>
  </nav>

  <aside class="abs cats">
    <h3><svg width="20" height="16" viewBox="0 0 20 16"><path d="M0 2h20M0 8h20M0 14h20" stroke="#fff" stroke-width="2"/></svg>SHOP BY CATEGORIES</h3>
    <ul>
      <li>Vases</li><li>Throw Pillows</li><li>Blankets and Throws</li><li>For Your Floors</li><li>For Your Walls</li><li>For Your Table</li><li>For Your Bedside</li><li>Let THere Be Light</li><li>Put Your Feet Up</li>
    </ul>
  </aside>

  <section class="abs hero" role="img" aria-label="Stack of folded throws and blankets topped with pillows">
    <div class="text">NEW<br>LOOK<br>VASES</div>
    <div class="badge">20%<small>OFF</small></div>
    <div class="shop">SHOP NOW »</div>
    <div class="dots"><i></i><i></i><i></i><i></i></div>
  </section>

  <div class="abs banner" style="left:98px;background:linear-gradient(135deg,#c9c2b8,#7b7670 60%,#e4e0da)" role="img" aria-label="Living room with vases and cushions"><div class="label">VASES</div></div>
  <div class="abs banner" style="left:441px;background:linear-gradient(180deg,#dfe7ea,#c28a5c 65%,#e9e6e0)" role="img" aria-label="Window seat with throw pillows"><div class="label">THROW PILLOWS</div></div>
  <div class="abs banner" style="left:783px;background:linear-gradient(180deg,#c5ccd0,#9da2a4 55%,#d6d3ce)" role="img" aria-label="Bright room with a blanket and throw"><div class="label">BLANKETS AND THROWS</div></div>

  <svg class="abs wave" style="top:951px" viewBox="0 0 1003 10" preserveAspectRatio="none"><rect width="1003" height="10" fill="url(#wavy)"/></svg>

  <h2 class="abs section-title" style="top:1006px"><span>Featured <em>Products</em></span></h2>

  <div class="abs tabs"><span class="on">Latest</span><span>Best Seller</span><span>Special</span><span>New Arrival</span></div>

  <div class="abs product" style="top:1161px;left:98px">
    <div class="img" style="background:linear-gradient(180deg,#fafafa,#ece7df)" role="img" aria-label="Small white patterned vases with flowers"></div>
    <div class="rate"><span class="stars"><svg class="star-on"><use href="#star"/></svg><svg class="star-on"><use href="#star"/></svg><svg class="star-on"><use href="#star"/></svg><svg class="star-off"><use href="#star"/></svg><svg class="star-off"><use href="#star"/></svg></span></div>
    <div class="pname">Product Name 1</div>
    <div class="price"><s>$156.00</s><b>$156.00</b></div>
  </div>
  <div class="abs product" style="top:1161px;left:356px">
    <div class="img" style="background:linear-gradient(135deg,#b53a4c,#3b4f7a 50%,#c96a2c)" role="img" aria-label="Pile of colourful throw pillows"></div>
    <div class="ribbon"><span>New</span></div>
    <div class="rate"><span class="stars"><svg class="star-on"><use href="#star"/></svg><svg class="star-on"><use href="#star"/></svg><svg class="star-on"><use href="#star"/></svg><svg class="star-off"><use href="#star"/></svg><svg class="star-off"><use href="#star"/></svg></span></div>
    <div class="pname">Product Name 2</div>
    <div class="price"><s>$156.00</s><b>$156.00</b></div>
  </div>
  <div class="abs product" style="top:1161px;left:613px">
    <div class="img" style="background:linear-gradient(180deg,#d7c9a8,#c6a66a 60%,#a4793f)" role="img" aria-label="Armchair with a cushion and throw"></div>
    <div class="rate"><span class="stars"><svg class="star-on"><use href="#star"/></svg><svg class="star-on"><use href="#star"/></svg><svg class="star-on"><use href="#star"/></svg><svg class="star-off"><use href="#star"/></svg><svg class="star-off"><use href="#star"/></svg></span></div>
    <div class="pname">Product Name 3</div>
    <div class="price"><s>$156.00</s><b>$156.00</b></div>
  </div>
  <div class="abs product" style="top:1161px;left:870px">
    <div class="img" style="background:linear-gradient(180deg,#dedbd3,#c9a47c 60%,#8e7357)" role="img" aria-label="Table lamp on a bedside table"></div>
    <div class="rate"><span class="stars"><svg class="star-on"><use href="#star"/></svg><svg class="star-on"><use href="#star"/></svg><svg class="star-on"><use href="#star"/></svg><svg class="star-off"><use href="#star"/></svg><svg class="star-off"><use href="#star"/></svg></span></div>
    <div class="pname">Product Name 4</div>
    <div class="price"><s>$156.00</s><b>$156.00</b></div>
  </div>

  <div class="abs product active" style="top:1550px;left:98px">
    <div class="img" style="background:linear-gradient(135deg,#e9e3d8,#b89a6a 55%,#d9d4cc)" role="img" aria-label="Candle holder on a patterned table runner"></div>
    <div class="rate"><span class="stars"><svg class="star-on"><use href="#star"/></svg><svg class="star-on"><use href="#star"/></svg><svg class="star-on"><use href="#star"/></svg><svg class="star-off"><use href="#star"/></svg><svg class="star-off"><use href="#star"/></svg></span></div>
    <div class="pname">Product Name 1</div>
    <div class="price"><s>$156.00</s><b>$156.00</b></div>
  </div>
  <div class="abs product" style="top:1550px;left:356px">
    <div class="img" style="background:linear-gradient(180deg,#3b2b20,#6b4a30 55%,#b98a55)" role="img" aria-label="Living room with fireplace and pendant lights"></div>
    <div class="rate"><span class="stars"><svg class="star-on"><use href="#star"/></svg><svg class="star-on"><use href="#star"/></svg><svg class="star-on"><use href="#star"/></svg><svg class="star-off"><use href="#star"/></svg><svg class="star-off"><use href="#star"/></svg></span></div>
    <div class="pname">Product Name 2</div>
    <div class="price"><s>$156.00</s><b>$156.00</b></div>
  </div>
  <div class="abs product" style="top:1550px;left:613px">
    <div class="img" style="background:linear-gradient(180deg,#ecebe7,#b7b2a8 60%,#e2e0db)" role="img" aria-label="Textured stone vase with greenery"></div>
    <div class="ribbon"><span>Sell</span></div>
    <div class="rate"><span class="stars"><svg class="star-on"><use href="#star"/></svg><svg class="star-on"><use href="#star"/></svg><svg class="star-on"><use href="#star"/></svg><svg class="star-off"><use href="#star"/></svg><svg class="star-off"><use href="#star"/></svg></span></div>
    <div class="pname">Product Name 3</div>
    <div class="price"><s>$156.00</s><b>$156.00</b></div>
  </div>
  <div class="abs product" style="top:1550px;left:870px">
    <div class="img" style="background:linear-gradient(180deg,#e6e1d6,#3a2e26 55%,#a89a86)" role="img" aria-label="Dark wood coffee table with a tray"></div>
    <div class="rate"><span class="stars"><svg class="star-on"><use href="#star"/></svg><svg class="star-on"><use href="#star"/></svg><svg class="star-on"><use href="#star"/></svg><svg class="star-off"><use href="#star"/></svg><svg class="star-off"><use href="#star"/></svg></span></div>
    <div class="pname">Product Name 4</div>
    <div class="price"><s>$156.00</s><b>$156.00</b></div>
  </div>

  <div class="abs actions">
    <i><svg width="14" height="13" viewBox="0 0 24 22"><path fill="#fff" d="M12 21 2 11a5.5 5.5 0 0 1 10-7 5.5 5.5 0 0 1 10 7z"/></svg></i>
    <i><svg width="15" height="13" viewBox="0 0 24 22"><path fill="#fff" d="M1 1h4l3 12h12l3-9H7"/><circle cx="9" cy="19" r="2" fill="#fff"/><circle cx="19" cy="19" r="2" fill="#fff"/></svg></i>
    <i><svg width="13" height="13" viewBox="0 0 24 24"><path d="M3 3l7 7M21 3l-7 7M3 21l7-7M21 21l-7-7" stroke="#fff" stroke-width="3"/></svg></i>
    <i><svg width="14" height="14" viewBox="0 0 24 24"><circle cx="10" cy="10" r="7" fill="none" stroke="#fff" stroke-width="3"/><path d="M15 15l7 7" stroke="#fff" stroke-width="3"/></svg></i>
  </div>

  <div class="abs viewall">VIEW ALL »</div>

  <svg class="abs wave" style="top:2054px" viewBox="0 0 1003 10" preserveAspectRatio="none"><rect width="1003" height="10" fill="url(#wavy)"/></svg>

  <h2 class="abs section-title" style="top:2111px"><span>Hot <em>Deals</em></span></h2>

  <div class="abs deal" style="left:98px">
    <div class="img" style="background:linear-gradient(180deg,#f3efec,#e9b9c7 45%,#f0eeea)" role="img" aria-label="Pink roses in glass vases"></div>
    <div class="body">
      <div class="stars"><svg class="star-on"><use href="#star"/></svg><svg class="star-on"><use href="#star"/></svg><svg class="star-on"><use href="#star"/></svg><svg class="star-off"><use href="#star"/></svg><svg class="star-off"><use href="#star"/></svg></div>
      <div class="pname">Product Name 1</div>
      <div class="price"><s>$156.00</s><b>$156.00</b></div>
      <div class="desc">Duis autem vel eum iriure dolom in hendrerit in vulputate velit essel molestie facilisi.</div>
    </div>
  </div>
  <div class="abs deal" style="left:613px">
    <div class="img" style="background:linear-gradient(180deg,#7a6e62,#d8c48a 55%,#ece8e1)" role="img" aria-label="Window seat lined with patterned cushions"></div>
    <div class="body">
      <div class="stars"><svg class="star-on"><use href="#star"/></svg><svg class="star-on"><use href="#star"/></svg><svg class="star-on"><use href="#star"/></svg><svg class="star-off"><use href="#star"/></svg><svg class="star-off"><use href="#star"/></svg></div>
      <div class="pname">Product Name 2</div>
      <div class="price"><s>$156.00</s><b>$156.00</b></div>
      <div class="desc">Duis autem vel eum iriure dolom in hendrerit in vulputate velit essel molestie facilisi.</div>
    </div>
  </div>

  <div class="abs band"></div>
  <div class="abs feature main" style="left:98px"><svg width="24" height="16" viewBox="0 0 26 18"><path fill="#0355a3" d="M0 0h16v13H0zM16 5h6l4 4v4h-10z"/><circle cx="5" cy="15" r="3" fill="#0355a3"/><circle cx="20" cy="15" r="3" fill="#0355a3"/></svg><span>FREE SHIPPING On Order<br>Over $99</span></div>
  <div class="abs feature" style="left:356px"><svg width="20" height="20" viewBox="0 0 24 24"><circle cx="12" cy="12" r="10" fill="none" stroke="#333" stroke-width="3"/><circle cx="12" cy="12" r="4" fill="none" stroke="#333" stroke-width="3"/></svg><span>Need Help<br>+1 555 014 2290</span></div>
  <div class="abs feature" style="left:613px"><svg width="22" height="14" viewBox="0 0 24 14"><rect x="1" y="1" width="22" height="12" fill="none" stroke="#333" stroke-width="2"/><circle cx="12" cy="7" r="3" fill="#333"/></svg><span>Money Back Guarantee</span></div>
  <div class="abs feature" style="left:870px"><svg width="20" height="17" viewBox="0 0 24 20"><path fill="#333" d="M8 0h8v4h8v16H0V4h8zm2 2v2h4V2z"/></svg><span>30 Days Return Service</span></div>

  <footer class="abs footer">
    <div class="flogo"><div class="name">norla</div><div class="sub">HOME GOODS</div></div>
    <p class="about">Ut wisi enim ad minim veniam, quis nostrud exercim ori tation ullamcorper suscipit lobortis nisl ut aliquip ex eal commodo consequat. Duis autem vel eum ok iriure dolor in hendrerit in vulputate velit esse molestie consequati.</p>
    <div class="fcol" style="left:508px"><h4>MY ACCOUNT</h4><ul><li>My Orders</li><li>My Credit Slips</li><li>My Addresses</li><li>My Personal Info</li></ul></div>
    <div class="fcol" style="left:710px"><h4>INFORMATION</h4><ul><li>Specials</li><li>New Products</li><li>Best Sellers</li><li>Our Stores</li><li>Contact Us</li></ul></div>
    <div class="fcol" style="left:903px"><h4>INFORMATION</h4>
      <div class="addr"><svg width="12" height="16" viewBox="0 0 12 16"><path fill="#fff" d="M6 0a6 6 0 0 1 6 6c0 4-6 10-6 10S0 10 0 6a6 6 0 0 1 6-6zm0 4a2 2 0 1 0 0 4 2 2 0 0 0 0-4z"/></svg><span>Norla Home Goods<br>48 Linden Row<br>Brookvale, NY 10012</span></div>
      <div class="addr" style="padding-left:22px">+1 555 014 2290</div>
      <div class="addr"><svg width="13" height="10" viewBox="0 0 24 18"><rect x="1" y="1" width="22" height="16" fill="#fff"/><path d="M1 1l11 9 11-9" stroke="#1c1c1c" stroke-width="2" fill="none"/></svg><span>info@norlahome.com</span></div>
    </div>
    <div class="news">
      <div class="mailbox"><svg width="20" height="14" viewBox="0 0 24 18"><rect x="1" y="1" width="22" height="16" fill="#fff"/><path d="M1 1l11 9 11-9" stroke="#0355a3" stroke-width="2" fill="none"/></svg></div>
      <span class="label">Newsletter Signup</span>
      <div class="input">Your e-mail</div>
      <div class="signup">SIGNUP</div>
    </div>
    <div class="social"><i></i><i></i><i></i><i></i></div>
  </footer>

  <div class="abs bottom">
    <span>Copyright © 2017 Norla Home Goods. All Right Reserved.</span>
    <div class="payments"><span>Mintpay</span><span>Cardeo</span><span>Tendrix</span><span>Orbis</span></div>
  </div>

</div>
</body>
</html>
```